Emergency Dental Referral Company

I need a brochure to advertise my business to prospective dentists that may want to join or to dentists that may want to use this for their own patients. I also need to advertise this brochure to ER physicians who see many dental emergencies. This brochure is meant to be dual purpose: advertise our company and services to the ER physicians who then hand out the brochures to the dental emergency patients in pain. See our website for further details at www.molarquickfix.com

I will also be attaching our logo design.

Target Market(s)

Emergency Room physicians and other medical personnel who will distribute these brochures to patients in dental pain and dental emergencies

Industry/Entity Type

Business

Font styles to use
Serif
Sans Serif

Requirements
Must have
• Must be simple! Must have a call to action- inspiration to go to website. Highlight our guarantee that states "If you are not seen by a dentist in 24 hours or less, you will receive your money back. Emphasis on the logo. Must discuss how we find a dentist in your zip code in three easy steps.
• For the color- please make similar to our website of www.molarquickfix.com
Nice to have
• Would like to state that this service can see patients at any hour of the day.
Should not have
• no contact information besides the URL. www.molarquickfix.com

```html
<!DOCTYPE html>
<html lang="en">
<head>
<meta charset="utf-8">
<title>Molar Quick Fix — Emergency Dentist Brochure</title>
<link rel="stylesheet" href="https://fonts.googleapis.com/css2?family=Oswald:wght@300;400;600&family=Open+Sans:wght@400&display=swap">
<style>
  :root {
    --blue: #1f7bc4;
    --blue-deep: #1565ad;
    --blue-light: #3b95d6;
    --green: #3cac49;
    --white: #ffffff;
    --paper: #f4f5f6;
    --ink: #6d6f72;
    --stage: #d9d9d9;
  }
  * { margin: 0; padding: 0; box-sizing: border-box; }
  html, body { width: 1200px; height: 900px; overflow: hidden; }
  body {
    background: linear-gradient(180deg, #f2f2f2 0%, var(--stage) 100%);
    font-family: "Oswald", "Arial Narrow", sans-serif;
    position: relative;
  }
  .page {
    position: absolute;
    top: 190px;
    width: 360px;
    height: 520px;
    background: var(--paper);
    overflow: hidden;
    box-shadow: 0 6px 18px rgba(0,0,0,.18);
  }
  .page svg { position: absolute; inset: 0; width: 360px; height: 520px; }
  .cover { left: 40px; }
  .spread-left { left: 440px; }
  .spread-right { left: 800px; }

  /* cover */
  .brand {
    position: absolute; top: 36px; left: 0; width: 100%;
    display: flex; justify-content: center; align-items: center; gap: 10px;
  }
  .brand-mark { width: 18px; height: 18px; background: var(--green); }
  .brand-name { font-weight: 600; font-size: 28px; color: var(--blue); letter-spacing: .5px; line-height: 1; }
  .guarantee {
    position: absolute; left: 0; width: 100%; top: 384px;
    text-align: center; color: var(--white); text-transform: uppercase;
    font-weight: 300; font-size: 19px; line-height: 1.2;
  }
  .guarantee strong { font-weight: 600; font-size: 27px; }
  .web-link {
    position: absolute; left: 0; width: 100%;
    text-align: center; color: var(--white);
    font-weight: 400; font-size: 13px; letter-spacing: .5px; line-height: 1;
  }
  .cover .web-link { top: 494px; }

  /* spread left */
  .headline-green {
    position: absolute; top: 22px; left: 18px;
    color: var(--white); text-transform: uppercase;
    font-weight: 300; font-size: 21px; line-height: 1.15;
  }
  .headline-green strong { font-weight: 600; font-size: 27px; display: block; }
  .emergency {
    position: absolute; left: 20px; top: 398px;
    color: var(--blue); text-transform: uppercase; line-height: 1.05;
    font-weight: 300; font-size: 30px;
  }
  .emergency strong { display: block; font-weight: 600; font-size: 32px; }
  .mission {
    position: absolute; left: 196px; top: 378px; width: 146px;
    font-family: "Open Sans", Arial, sans-serif; font-size: 8.6px;
    line-height: 1.7; color: var(--ink); text-align: justify;
  }

  /* spread right */
  .service-name {
    position: absolute; left: 20px; top: 102px; width: 120px;
    text-align: center; color: var(--white); text-transform: uppercase;
    font-weight: 300; font-size: 22px; line-height: 1.15;
  }
  .steps-title {
    position: absolute; left: 20px; top: 292px;
    color: var(--white); text-transform: uppercase;
    font-weight: 300; font-size: 19px; line-height: 1.15;
  }
  .steps-title strong { font-weight: 600; }
  .step-name {
    position: absolute; width: 80px; text-align: center; line-height: 1;
    color: var(--blue); font-weight: 600; font-size: 18px;
  }
  .step-label {
    position: absolute; width: 110px; text-align: center; line-height: 1;
    color: var(--white); text-transform: uppercase;
    font-weight: 400; font-size: 10.5px;
  }
  .spread-right .web-link { top: 494px; }
</style>
</head>
<body>

<section class="page cover">
  <svg viewBox="0 0 360 520">
    <defs>
      <linearGradient id="coverPhotoA" x1="0" y1="0" x2="0" y2="1">
        <stop offset="0" stop-color="#ece3dc"/>
        <stop offset="1" stop-color="#f4f5f6"/>
      </linearGradient>
      <linearGradient id="coverPhotoB" x1="0" y1="0" x2="0" y2="1">
        <stop offset="0" stop-color="#efe6de"/>
        <stop offset="1" stop-color="#f2f3f5"/>
      </linearGradient>
    </defs>
    <polygon points="180,0 360,0 360,260" fill="#eceef1"/>
    <polygon role="img" aria-label="Photo of a female doctor with a stethoscope" points="0,90 150,90 150,330 0,390" fill="url(#coverPhotoA)"/>
    <polygon role="img" aria-label="Photo of a male doctor in a white coat" points="210,90 360,90 360,290 255,190" fill="url(#coverPhotoB)"/>
    <polygon points="0,390 255,190 360,290 360,520 0,520" fill="var(--blue)"/>
  </svg>
  <div class="brand"><span class="brand-mark"></span><span class="brand-name">Molar Quick Fix</span></div>
  <p class="guarantee">If you are not seen by a<br><strong>Dentist</strong> in <strong>24 hours</strong><br>or less you will receive<br>your money back</p>
  <p class="web-link">www.molarquickfix.com</p>
</section>

<section class="page spread-left">
  <svg viewBox="0 0 360 520">
    <defs>
      <linearGradient id="handPhoto" x1="0" y1="0" x2="1" y2="1">
        <stop offset="0" stop-color="#d4c8de"/>
        <stop offset="1" stop-color="#d3a792"/>
      </linearGradient>
      <linearGradient id="toolsPhoto" x1="0" y1="0" x2="1" y2="1">
        <stop offset="0" stop-color="#e2dcbd"/>
        <stop offset="1" stop-color="#cfd9e1"/>
      </linearGradient>
    </defs>
    <polygon points="0,0 300,0 300,10 140,200 0,300" fill="var(--green)"/>
    <polygon points="300,0 360,0 360,150 300,10" fill="var(--blue-deep)"/>
    <polygon role="img" aria-label="Photo of an open hand holding a pill" points="160,140 255,240 160,340 60,240" fill="url(#handPhoto)"/>
    <polygon role="img" aria-label="Photo of dental instruments and a denture model" points="300,10 360,80 360,330 260,220 300,150" fill="url(#toolsPhoto)"/>
  </svg>
  <p class="headline-green">Get seen within<strong>24 hours</strong>or your money back!</p>
  <h2 class="emergency">Your<strong>Emergency<br>Dentist</strong></h2>
  <p class="mission">Our mission plain and simple is to get you seen by a qualified dentist as quickly as possible to get you out of pain. Nobody likes pain and no one should have to live with it. If we can get you seen by a dentist in 24 hours or less, we have succeeded.</p>
</section>

<section class="page spread-right">
  <svg viewBox="0 0 360 520">
    <defs>
      <linearGradient id="clinicPhoto" x1="0" y1="0" x2="1" y2="1">
        <stop offset="0" stop-color="#eef1ef"/>
        <stop offset="1" stop-color="#dde5dc"/>
      </linearGradient>
      <linearGradient id="dentistPhoto" x1="0" y1="0" x2="0" y2="1">
        <stop offset="0" stop-color="#efe2cc"/>
        <stop offset="1" stop-color="#f5f6f7"/>
      </linearGradient>
      <linearGradient id="nursePhoto" x1="0" y1="0" x2="0" y2="1">
        <stop offset="0" stop-color="#ecdcd0"/>
        <stop offset="1" stop-color="#b9d8e8"/>
      </linearGradient>
    </defs>
    <rect role="img" aria-label="Photo of a dental treatment room" x="0" y="0" width="360" height="300" fill="url(#clinicPhoto)"/>
    <polygon points="0,0 80,0 0,120" fill="var(--blue-deep)"/>
    <polygon points="0,130 80,45 165,135 80,225 0,190" fill="var(--green)"/>
    <polygon role="img" aria-label="Photo of a smiling female dentist" points="120,165 250,165 265,245 170,335 110,280" fill="url(#dentistPhoto)"/>
    <polygon role="img" aria-label="Photo of a nurse holding an apple" points="290,100 360,90 360,335 290,300" fill="url(#nursePhoto)"/>
    <polygon points="0,250 170,335 265,245 360,335 360,520 0,520" fill="var(--blue)"/>
    <g fill="var(--white)">
      <rect x="38" y="378" width="64" height="64" transform="rotate(45 70 410)"/>
      <rect x="148" y="363" width="64" height="64" transform="rotate(45 180 395)"/>
      <rect x="258" y="348" width="64" height="64" transform="rotate(45 290 380)"/>
    </g>
    <g fill="none" stroke="var(--green)" stroke-width="4.5" stroke-linecap="round" stroke-linejoin="round">
      <polyline points="61,391 68,398 80,383"/>
      <polyline points="171,376 178,383 190,368"/>
      <polyline points="281,361 288,368 300,353"/>
    </g>
  </svg>
  <p class="service-name">Molar<br>Quick Fix</p>
  <p class="steps-title">Find a<br>dentist in<br><strong>3</strong> easy <strong>steps</strong></p>
  <span class="step-name" style="left:30px;top:408px">STEP 1</span>
  <span class="step-name" style="left:140px;top:393px">STEP 2</span>
  <span class="step-name" style="left:250px;top:378px">STEP 3</span>
  <span class="step-label" style="left:15px;top:466px">Fill out a form</span>
  <span class="step-label" style="left:125px;top:451px">Find a dentist</span>
  <span class="step-label" style="left:235px;top:436px">Get your appointment</span>
  <p class="web-link">Start now at www.molarquickfix.com</p>
</section>

</body>
</html>
```